Modern Catering Company needs Letterhead Design

We need a letterhead design that will make effective use of the corporate logo and color scheme, along with careful typography, helps this letterhead design communicate the brand well. We do have a corporate logo, however feel free to enhance the color scheme with gold and purple. We are serving a very upscale clientele so the letterhead has to reflect elegance, professionalism, cleanliness, and modern style. We are branding the company so the letterhead and business cards must fit the brand story. There should be no cartoonish elements in the design and we are looking for sharper lines.

Target Market(s)

Businesses and upscale clientele

Industry/Entity Type

Catering

Contact Information for Business Card

while this design can have any number of quirks and distinctions, it needs to be cohesive with the entire brand story clean, professional but edgy

Requirements
Must have
• must have good and carefully placement of it’s logo and where you place the text or the message. Colors blue, very deep purple, jewel tones not pastels, gold. Blue must be the primary color you may accent with purple or gold. Contact information is as follows: Co-Owners/ Chefs: R. Hollowmere & L. Brandt, phone: 414-555-0182 email:Contact@orchardtablecatering.example, address: 6127 W Larkspur Hollow Rd, Milwaukee, WI 53299
Should not have
• pastel colors, Do not add the BBQ information to the letterhead or business card it was a mistake by the previous designer.

```html
<!DOCTYPE html>
<html lang="en">
<head>
<meta charset="UTF-8">
<title>Orchard Table Catering – Letterhead</title>
<link href="https://fonts.googleapis.com/css2?family=Open+Sans:wght@400;600&display=swap" rel="stylesheet">
<style>
  :root {
    --backdrop: #d9d9d9;
    --paper: #ffffff;
    --brand-blue: #3a6db5;
    --brand-blue-deep: #2f5da0;
    --ink: #2b2b2b;
    --signature-tone: #ececec;
  }
  * { box-sizing: border-box; margin: 0; padding: 0; }
  html, body {
    width: 1200px;
    height: 1015px;
    overflow: hidden;
    background: var(--backdrop);
    font-family: "Open Sans", Arial, sans-serif;
  }
  .letterhead {
    position: absolute;
    left: 232px;
    top: 32px;
    width: 736px;
    height: 952px;
    background: var(--paper);
    box-shadow: 0 6px 18px rgba(0, 0, 0, 0.18);
    overflow: hidden;
  }
  .brand {
    position: absolute;
    top: 52px;
    left: 0;
    width: 100%;
    text-align: center;
    color: var(--brand-blue);
    font-weight: 600;
    text-transform: uppercase;
  }
  .brand-mark {
    display: block;
    width: 12px;
    height: 12px;
    margin: 0 auto 10px;
    border-radius: 50%;
    background: var(--brand-blue);
  }
  .brand-name {
    display: block;
    font-size: 24px;
    line-height: 1.1;
    letter-spacing: 0.04em;
  }
  .brand-sub {
    display: block;
    margin-top: 4px;
    font-size: 11px;
    line-height: 1.2;
    letter-spacing: 0.55em;
    padding-left: 0.55em;
  }
  .letter-body {
    position: absolute;
    top: 176px;
    left: 78px;
    width: 580px;
    color: var(--ink);
    font-size: 10.5px;
    line-height: 1.55;
  }
  .letter-body p { margin-bottom: 16px; }
  .signature {
    position: absolute;
    top: 552px;
    left: 78px;
    width: 140px;
    height: 56px;
    background: var(--signature-tone);
    border-radius: 4px;
  }
  .footer-band {
    position: absolute;
    left: 0;
    bottom: 0;
    width: 100%;
    height: 260px;
  }
  .contact {
    position: absolute;
    left: 34px;
    bottom: 26px;
    color: var(--paper);
    font-size: 10px;
    line-height: 1.8;
    list-style: none;
  }
  .contact li { display: flex; align-items: center; gap: 6px; }
  .contact svg { width: 10px; height: 10px; fill: var(--paper); flex: none; }
</style>
</head>
<body>
  <main class="letterhead">
    <header class="brand">
      <span class="brand-mark"></span>
      <span class="brand-name">Orchard Table</span>
      <span class="brand-sub">Catering</span>
    </header>

    <section class="letter-body">
      <p>Lorem Ipsum is simply dummy text of the printing and typesetting industry. Lorem Ipsum has been the industry's standard dummy text ever since the 1500s, when an unknown printer took a galley of type and scrambled it to make a type specimen book. It has survived not only five centuries, but also the leap into electronic typesetting, remaining essentially unchanged. It was popularised in the 1960s with the release of Pressmark sheets containing Lorem Ipsum passages, and more recently with desktop publishing software like Quillset Layout including versions of Lorem Ipsum.</p>
      <p>It is a long established fact that a reader will be distracted by the readable content of a page when looking at its layout. The point of using Lorem Ipsum is that it has a more-or-less normal distribution of letters, as opposed to using 'Content here, content here', making it look like readable English. Many desktop publishing packages and web page editors now use Lorem Ipsum as their default model text, and a search for 'lorem ipsum' will uncover many web sites still in their infancy. Various versions have evolved over the years, sometimes by accident, sometimes on purpose (injected humour and the like).</p>
      <p>Contrary to popular belief, Lorem Ipsum is not simply random text. It has roots in a piece of classical Latin literature from 45 BC, making it over 2000 years old. A Latin professor at a small college looked up one of the more obscure Latin words, consectetur, from a Lorem Ipsum passage, and going through the cites of the word in classical literature, discovered the undoubtable source. Lorem Ipsum comes from sections 1.10.32 and 1.10.33 of "de Ordine Rerum" (The Order of Things) by Varenius, written in 45 BC. This book is a treatise on the theory of ethics, very popular during the Renaissance. The first line of Lorem Ipsum, "Lorem ipsum dolor sit amet..", comes from a line in section 1.10.32.</p>
    </section>

    <div class="signature" role="img" aria-label="Handwritten signature of the co-owner"></div>

    <svg class="footer-band" viewBox="0 0 736 260" preserveAspectRatio="none" aria-hidden="true">
      <path d="M0 170 C 220 130, 440 150, 736 70 L736 260 L0 260 Z" fill="var(--brand-blue)"/>
      <path d="M0 160 C 220 118, 440 138, 736 56" fill="none" stroke="var(--brand-blue-deep)" stroke-width="3"/>
    </svg>

    <ul class="contact">
      <li><svg viewBox="0 0 10 10"><path d="M2 0.5 L3.6 0.5 L4.2 2.8 L3 3.6 C3.6 5 4.9 6.4 6.4 7 L7.2 5.8 L9.5 6.4 L9.5 8 C9.5 9 8.7 9.5 8 9.5 C4 9.2 0.8 6 0.5 2 C0.5 1.3 1 0.5 2 0.5 Z"/></svg>414-555-0182</li>
      <li><svg viewBox="0 0 10 10"><path d="M0.5 2 H9.5 V8 H0.5 Z M1 2.4 L5 5.6 L9 2.4" stroke="var(--brand-blue)" stroke-width="0.8"/></svg>Contact@orchardtablecatering.example</li>
      <li><svg viewBox="0 0 10 10"><path d="M5 0.5 C3 0.5 1.8 2 1.8 3.7 C1.8 6 5 9.5 5 9.5 C5 9.5 8.2 6 8.2 3.7 C8.2 2 7 0.5 5 0.5 Z"/></svg>6127 W Larkspur Hollow Rd, Milwaukee, WI 53299</li>
    </ul>
  </main>
</body>
</html>
```